Vextara website

Web design for small consulting firm
It can be simple, easy to find approach

The primary use is business to business for

a. people wanting to find out a bit more of us after receiving a business card
b. Search words to draw people from search engines to us

Target Market(s)

Senior staff of large companies, in their work capacity
MD / CEO / CFO , directors, etc.

Industry/Entity Type

Business

Colors
ffffff
f79020
faa54b
33a6d7

```html
<!DOCTYPE html>
<html lang="en">
<head>
<meta charset="utf-8">
<title>Vextara</title>
<link rel="stylesheet" href="https://fonts.googleapis.com/css2?family=Open+Sans:ital,wght@0,400;0,600;0,700;1,400&display=swap">
<style>
:root{
  --orange:#e8862a;
  --orange-bright:#f79020;
  --orange-soft:#faa54b;
  --blue:#0075bb;
  --blue-light:#33a6d7;
  --blue-dark:#1f5a96;
  --white:#ffffff;
  --ink:#333333;
  --muted:#777777;
  --grey-logo:#a9a9a9;
  --footer:#e2e2e2;
}
*{margin:0;padding:0;box-sizing:border-box}
html,body{width:1024px;height:1200px;overflow:hidden}
body{position:relative;background:var(--white);font-family:"Open Sans",Arial,sans-serif;color:var(--ink)}
.abs{position:absolute}

/* header */
.brand{left:137px;top:10px;height:56px;display:flex;align-items:center}
.brand-name{font-size:36px;font-weight:700;color:var(--blue);line-height:1;letter-spacing:-.5px}
.social{display:flex;gap:12px}
.social span{width:20px;height:20px;border-radius:50%;background:var(--blue-dark)}
.social span.light{background:var(--blue-light)}
.header-social{left:810px;top:16px}
.callus{left:664px;top:41px;display:flex;align-items:center;gap:6px;font-size:13px;font-weight:600;color:var(--muted);letter-spacing:.3px}
.callus b{color:var(--orange-bright);font-weight:600}
.callus .ico{width:17px;height:17px;background:var(--orange-bright);border-radius:3px;display:flex;align-items:center;justify-content:center}

/* nav */
.nav{left:0;top:75px;width:1024px;height:41px;background:var(--orange)}
.nav ul{list-style:none;position:absolute;left:142px;width:746px;top:0;height:41px;display:flex;justify-content:space-between;align-items:center}
.nav li{color:var(--white);font-size:13px;font-weight:600;letter-spacing:2px}

/* hero */
.hero{left:0;top:116px;width:1024px;height:378px;background:linear-gradient(100deg,#8a6a55 0%,#c9a58c 30%,#e7d2c2 50%,#dfe6ee 65%,#9ab1c6 85%,#cdd8e2 100%)}
.hero-box{left:0;top:302px;width:534px;height:150px;background:rgba(230,110,20,.85);padding:18px 0 0 137px;color:var(--white)}
.hero-box h1{font-size:25px;font-weight:700;letter-spacing:.5px}
.hero-box p{font-size:15px;line-height:20px;margin-top:14px;width:360px}

/* blue band */
.band{left:0;top:494px;width:1024px;height:314px;background:var(--blue)}
.col{position:absolute;top:0;width:238px;color:var(--white)}
.col h2{font-size:19px;font-weight:400;margin-top:26px;padding-left:2px;height:29px}
.rule{height:4px;border-top:1px dotted rgba(160,210,240,.7);border-bottom:1px dotted rgba(160,210,240,.7)}
.photo{height:109px;margin-top:13px;border-radius:3px}
.col p{font-size:9.6px;line-height:14.4px;margin-top:19px}
.col a{display:inline-block;margin-top:13px;font-size:10px;font-weight:700;color:var(--white);text-decoration:underline}

/* clients & news */
.sec-title{font-size:19px;font-weight:400;color:#444;height:39px;display:flex;align-items:center;gap:9px;padding-left:2px}
.grey-rule{height:4px;border-top:1px dotted #bbb;border-bottom:1px dotted #bbb}
.clients{left:137px;top:830px;width:480px}
.logos{display:flex;justify-content:space-between;align-items:center;margin-top:20px;height:48px}
.logos div{display:flex;align-items:center;gap:6px;font-size:14px;font-weight:700;color:var(--grey-logo)}
.logos i{display:block;width:14px;height:14px;border-radius:50%;background:var(--grey-logo)}
.quote{font-size:13.4px;font-style:italic;line-height:20px;color:#555;margin-top:28px}
.author{font-size:10px;font-weight:700;color:var(--blue);margin-top:10px}

.news{left:649px;top:830px;width:240px}
.news h3{font-size:12px;font-weight:600;color:#333;margin-top:8px;letter-spacing:.2px}
.item{display:flex;gap:13px;margin-top:7px}
.thumb{width:68px;height:58px;flex:none}
.item p{font-size:9.4px;line-height:14.4px;color:var(--muted)}
.date{font-size:8px;font-weight:700;color:var(--muted);margin-top:4px;display:flex;gap:4px;align-items:center}

/* footer */
.footer{left:0;top:1116px;width:1024px;height:84px;background:var(--footer)}
.links{left:138px;top:28px;font-size:10px;font-weight:700;color:#333;letter-spacing:.8px;word-spacing:3px}
.copy{left:137px;top:51px;font-size:9.6px;color:#444}
.footer-social{left:396px;top:25px;gap:12px}
.footer-social span{width:21px;height:21px}
.contact{left:745px;top:24px;font-size:9.6px;color:#333;display:flex;flex-direction:column;gap:13px}
.contact div{display:flex;align-items:center;gap:14px}
</style>
</head>
<body>

<header>
  <div class="abs brand"><div class="brand-name">Vextara</div></div>
  <div class="abs social header-social"><span></span><span class="light"></span><span></span></div>
  <div class="abs callus">
    <span class="ico"><svg width="11" height="11" viewBox="0 0 24 24"><path fill="#fff" d="M6.6 10.8a15.1 15.1 0 0 0 6.6 6.6l2.2-2.2c.3-.3.7-.4 1-.2 1.1.4 2.3.6 3.6.6.6 0 1 .4 1 1V20c0 .6-.4 1-1 1A17 17 0 0 1 3 4c0-.6.4-1 1-1h3.5c.6 0 1 .4 1 1 0 1.3.2 2.5.6 3.6.1.3 0 .7-.2 1z"/></svg></span>
    CALL US TODAY <b>+1800.555.0147</b>
  </div>
</header>

<nav class="abs nav"><ul><li>HOME</li><li>SERVICES</li><li>BLOG</li><li>ABOUT</li><li>CLIENTS</li><li>CONTACT</li></ul></nav>

<section class="abs hero" role="img" aria-label="Photo of a smiling team of young business people"></section>
<div class="abs hero-box">
  <h1>We Bring Businesses Forward</h1>
  <p>It is a long established fact that a reader will be distracted by the readable content of a page when looking at its layout.</p>
</div>

<section class="abs band">
  <div class="col" style="left:137px">
    <h2>Who We Are</h2><div class="rule"></div>
    <div class="photo" role="img" aria-label="Photo of a business team meeting" style="background:linear-gradient(90deg,#9aa3ae,#3b3f46 55%,#6d7580)"></div>
    <p>Lorem ipsum dolor sit amet, consectetur adipisicing elit, sed do eiusmod tempor incididunt ut labore et dolore magna aliqua. Ut enim ad minim veniam, quis nostrud exercitation.</p>
    <a>READ MORE</a>
  </div>
  <div class="col" style="left:391px">
    <h2>Our Values</h2><div class="rule"></div>
    <div class="photo" role="img" aria-label="Photo of two businessmen in conversation" style="background:linear-gradient(90deg,#dfe3e6,#3a4350 40%,#eceef0 60%,#4d535c)"></div>
    <p>Lorem ipsum dolor sit amet, consectetur adipisicing elit, sed do eiusmod tempor incididunt ut labore et dolore magna aliqua. Ut enim ad minim veniam, quis nostrud exercitation.</p>
    <a>READ MORE</a>
  </div>
  <div class="col" style="left:649px">
    <h2>What We Do</h2><div class="rule"></div>
    <div class="photo" role="img" aria-label="Photo of two colleagues working at a laptop" style="background:linear-gradient(180deg,#dfe7ef,#8ea7c6 55%,#a0735a)"></div>
    <p>Lorem ipsum dolor sit amet, consectetur adipisicing elit, sed do eiusmod tempor incididunt ut labore et dolore magna aliqua. Ut enim ad minim veniam, quis nostrud exercitation.</p>
    <a>READ MORE</a>
  </div>
</section>

<section class="abs clients">
  <h2 class="sec-title">Our Clients</h2>
  <div class="grey-rule"></div>
  <div class="logos">
    <div><i></i>Norbridge</div>
    <div><i></i>Hueline</div>
    <div><i></i>Talkwave</div>
    <div><i></i>Geckora</div>
  </div>
  <p class="quote">“Lorem ipsum dolor sit amet, consectetur adipisicing elit, sed do eiusmod tempor incididunt ut labore et dolore magna aliqua. Ut enim ad minim veniam, quis nostrud exercitation. Lorem ipsum dolor sit amet, consectetur adipisicing elit, sed do eiusmod tempor incididunt ut labore et dolore magna aliqua.”</p>
  <p class="author">JANE MORROW, Halden Group</p>
</section>

<section class="abs news">
  <h2 class="sec-title">
    <svg width="15" height="15" viewBox="0 0 16 16"><rect x="1.5" y="3" width="13" height="11.5" fill="none" stroke="#888" stroke-width="1.5"/><rect x="1.5" y="3" width="13" height="3" fill="#888"/><rect x="4" y="1" width="1.6" height="3" fill="#888"/><rect x="10.4" y="1" width="1.6" height="3" fill="#888"/></svg>
    Latest News</h2>
  <div class="grey-rule"></div>
  <h3>There are many variations of passages</h3>
  <div class="item">
    <div class="thumb" role="img" aria-label="Photo of a business team" style="background:linear-gradient(135deg,#c9d6e3,#4b5a6b)"></div>
    <div><p>The point of using Lorem Ipsum is that it has a more-or-less normal distribution of letters, as opposed..</p><div class="date"><svg width="8" height="8" viewBox="0 0 16 16"><rect x="1.5" y="3" width="13" height="11.5" fill="none" stroke="#999" stroke-width="2"/></svg>8 December 2013</div></div>
  </div>
  <h3 style="margin-top:14px">All the Lorem Ipsum generators</h3>
  <div class="item">
    <div class="thumb" role="img" aria-label="Photo of a businessman signing documents" style="background:linear-gradient(135deg,#3a3d44,#b8c2cc)"></div>
    <div><p>The point of using Lorem Ipsum is that it has a more-or-less normal distribution of letters, as opposed..</p><div class="date"><svg width="8" height="8" viewBox="0 0 16 16"><rect x="1.5" y="3" width="13" height="11.5" fill="none" stroke="#999" stroke-width="2"/></svg>8 December 2013</div></div>
  </div>
</section>

<footer class="abs footer">
  <div class="abs links">LINKS &nbsp;| &nbsp;LINKS &nbsp;| &nbsp;LINKS &nbsp;| &nbsp;LINKS</div>
  <div class="abs copy">Copyright © 2014. All rights reserved. &nbsp;Company Name</div>
  <div class="abs social footer-social"><span></span><span class="light"></span><span></span></div>
  <div class="abs contact">
    <div><svg width="16" height="12" viewBox="0 0 16 12"><rect width="16" height="12" rx="1" fill="#777"/><path d="M1 1l7 6 7-6" fill="none" stroke="#e2e2e2" stroke-width="1.3"/></svg>info@vextara-mail.com</div>
    <div><svg width="16" height="14" viewBox="0 0 24 24"><path fill="#777" d="M6.6 10.8a15.1 15.1 0 0 0 6.6 6.6l2.2-2.2c.3-.3.7-.4 1-.2 1.1.4 2.3.6 3.6.6.6 0 1 .4 1 1V20c0 .6-.4 1-1 1A17 17 0 0 1 3 4c0-.6.4-1 1-1h3.5c.6 0 1 .4 1 1 0 1.3.2 2.5.6 3.6.1.3 0 .7-.2 1z"/></svg>890-55501-20470</div>
  </div>
</footer>

</body>
</html>
```